Immobilienmaklerin, Verkauf von Immobilien, Zielgruppe sind potentielle Eigentümer die ggf. Ihre Immobilie verkaufen möchten
Ich möchte nach erfolgreichem Verkauf einer Immobilie in der Nachbarschaft Postkarten verteilen, mit dem Hinweis, dass ich dort erfolgreich und in kürzester Zeit zum maximalen Preis eine Immobilie verkauft habe. Es soll dann möglich sein, dass ich in dem erstellten Design jeweils dann auf der Vorderseite 1-2 Immobilienbilder austauschen kann. Es soll ein Eyecatcher sein, edel und chic und vorallem sehr seriös sein.
Auf der Rückseite soll dann ein Gutschein für eine kostenlose Immobilienbewertung im Wert von 500,-€ sein und ein entsprechender Text, ob man selbst auch mit dem Gedanken spielt seine Immobilie zu veräußern. Ggf mit einem schönen Slogan. Gerne darf ein Foto von mir mit eingearbeitet werden. Ansonsten soll es in den Farben Schwarz, Gold sein passend zum Logo und gerne mit Elementen die aus dem Logo übernommen werden.
Am Besten wahrscheinlich im A5 Format quer
Hinweis: Immobilienkompetenz seit über 17 Jahren.
Ihre Immobilienmaklerin mit Herz im Rhein-Sieg-Kreis, Bonn, Köln
Denn wir gehen mit viel Herz für Sie die
sprichwörtliche Extrameile. Genau das ist es,
was den Unterschied macht: einen Mehrwert
durch beste fachliche Qualifizierung, hohes
Engagement, Ehrlichkeit und Fingerspitzengefühl
zu schaffen.
Eine Entscheidung fürs Leben.
Wir begleiten Sie sehr gerne.
Wissen, woran man ist. Kennen Sie den wirklich
erzielbaren Wert Ihrer Immobilie?
Wir schon.
Lassen Sie sich unverbindlich und kostenfrei
beraten. Gerne kommen wir Sie und Ihre Immobilie
besuchen und beantworten Ihnen alle
Fragen rund um den Verkauf oder die Vermietung
Ihrer Immobilie.
Nutzen Sie hierfür einfach unseren Gutschein
zur kostenlosen Wertermittlung.
Wir freuen uns auf Ihren Anruf!
Brauchen Sie einen Immobilienmakler? Unbedingt!
Margarete Hülsing, Geschäftsführerin.
Kauffrau der Grundstücks- und Wohnungswirtschaft

```html
<!DOCTYPE html>
<html lang="de">
<head>
<meta charset="utf-8">
<title>Hülsing Immobilien – Postkarte A5 quer</title>
<link rel="stylesheet" href="https://fonts.googleapis.com/css2?family=Open+Sans:wght@400;600;700&display=swap">
<style>
  :root {
    --ink: #353130;
    --ink-deep: #2a2726;
    --gold: #bb9a63;
    --gold-light: #d4b887;
    --paper: #ffffff;
    --stage-top: #6e6c6a;
    --stage-bottom: #1f1d1d;
    --text-dark: #2b2828;
  }
  * { box-sizing: border-box; margin: 0; padding: 0; }
  html, body { width: 909px; height: 1200px; overflow: hidden; }
  body {
    font-family: "Open Sans", Arial, sans-serif;
    background: radial-gradient(ellipse at 50% 0%, var(--stage-top) 0%, #383635 45%, var(--stage-bottom) 100%);
    position: relative;
  }
  .card {
    position: absolute;
    left: 66px;
    width: 777px;
    height: 548px;
    overflow: hidden;
    box-shadow: 0 6px 18px rgba(0,0,0,.45);
    background: var(--ink);
  }
  .card--front { top: 30px; }
  .card--back { top: 610px; }

  /* ---------- Front ---------- */
  .front-header {
    position: absolute; left: 0; top: 0; width: 100%; height: 118px;
    display: flex; align-items: center; justify-content: space-between;
    padding: 0 34px;
  }
  .brand {
    font-weight: 600; font-size: 19px; letter-spacing: 3px; text-transform: uppercase;
    color: var(--paper); display: flex; align-items: center; gap: 10px;
  }
  .brand__dot { width: 12px; height: 12px; border-radius: 50%; background: var(--gold); }
  .headline {
    font-weight: 700; font-size: 27px; line-height: 1.2; color: var(--paper); text-align: right;
  }
  .headline em { font-style: normal; color: var(--gold); }
  .gallery {
    position: absolute; left: 0; top: 118px; width: 100%; height: 252px;
    background: var(--gold); padding: 7px; display: flex; gap: 7px;
  }
  .photo-house { flex: 1; }
  .photo-house--a { background: linear-gradient(170deg, #b9cfe0 0%, #5d6b86 38%, #4f6a3a 64%, #5f9a3a 100%); }
  .photo-house--b { background: linear-gradient(190deg, #a9c4da 0%, #4e5a78 40%, #4b7a32 66%, #6cab3f 100%); }
  .front-info {
    position: absolute; left: 0; top: 370px; width: 100%; height: 138px;
  }
  .portrait-frame {
    position: absolute; left: 34px; top: 320px; width: 150px; height: 188px;
    background: var(--gold); padding: 6px; z-index: 2;
  }
  .photo-portrait {
    width: 100%; height: 100%;
    background: linear-gradient(160deg, #8a8d93 0%, #c9b59d 45%, #4a4a52 100%);
  }
  .agent-intro {
    position: absolute; left: 210px; top: 392px; color: var(--paper); font-size: 14px; line-height: 1.45;
  }
  .agent-intro strong { font-weight: 700; font-size: 16px; }
  .agent-intro strong span { color: var(--gold); }
  .experience {
    position: absolute; right: 34px; top: 400px; width: 196px;
    border: 1.5px solid var(--gold); color: var(--paper);
    font-size: 13px; line-height: 1.35; text-align: center; padding: 9px 8px;
  }
  .experience span { color: var(--gold); font-weight: 600; }
  .front-footer {
    position: absolute; left: 0; bottom: 0; width: 100%; height: 40px;
    background: var(--gold); display: flex; align-items: center; justify-content: flex-end;
    padding: 0 24px 0 210px; gap: 14px; color: var(--paper); font-size: 13px;
  }
  .front-footer__rule { flex: 1; height: 1.5px; background: var(--paper); }
  .front-footer svg { width: 20px; height: 20px; }

  /* ---------- Back ---------- */
  .back-copy {
    position: absolute; left: 30px; top: 38px; width: 440px;
    color: var(--paper); font-size: 15.6px; line-height: 22.6px;
  }
  .back-copy p + p { margin-top: 22.6px; }
  .voucher {
    position: absolute; left: 0; top: 425px; width: 489px; height: 89px;
    background: var(--gold); color: var(--paper); text-align: center; padding-top: 10px;
  }
  .voucher__title { font-size: 16.5px; }
  .voucher__value { font-size: 15px; display: flex; align-items: baseline; justify-content: center; gap: 8px; margin-top: -2px; }
  .voucher__value strong { font-size: 40px; font-weight: 700; line-height: 1.05; }
  .gold-rule {
    position: absolute; left: 489px; top: 0; width: 6px; height: 100%; background: var(--gold);
  }
  .contact-panel {
    position: absolute; left: 495px; top: 0; width: 282px; height: 100%;
    background: var(--paper);
  }
  .contact-panel .brand {
    color: var(--text-dark); justify-content: center; font-size: 17px; margin-top: 95px; letter-spacing: 2.5px;
  }
  .contact-portrait {
    position: absolute; left: 35px; top: 151px; width: 212px; height: 211px;
    background: var(--gold); padding: 7px;
  }
  .contact-details {
    position: absolute; left: 35px; top: 376px; color: var(--text-dark); font-size: 13px; line-height: 19px;
  }
  .contact-details h2 { font-size: 18px; font-weight: 700; line-height: 24px; }
  .contact-details h2 span, .contact-details .qualification { color: var(--gold); }
  .contact-details .line { font-size: 14.5px; line-height: 22.5px; }
  .contact-details .line b { color: var(--gold); font-weight: 700; }
</style>
</head>
<body>

<section class="card card--front" aria-label="Vorderseite">
  <header class="front-header">
    <div class="brand"><span class="brand__dot"></span>Hülsing Immobilien</div>
    <h1 class="headline">Brauchen Sie einen <em>Immobi-<br>lienmakler?</em> Unbedingt!</h1>
  </header>
  <div class="gallery">
    <div class="photo-house photo-house--a" role="img" aria-label="Foto eines verkauften Einfamilienhauses mit Rasen"></div>
    <div class="photo-house photo-house--b" role="img" aria-label="Zweites Foto des Hauses von der Seite"></div>
  </div>
  <div class="portrait-frame">
    <div class="photo-portrait" role="img" aria-label="Porträtfoto der Maklerin"></div>
  </div>
  <p class="agent-intro">
    <strong>Margarete <span>Hülsing</span></strong><br>
    Ihre Immobilienmaklerin mit Herz<br>
    im Rhein-Sieg-Kreis, Bonn, Köln
  </p>
  <p class="experience">Immobilienkompetenz<br>seit über <span>17 Jahre</span></p>
  <footer class="front-footer">
    <span class="front-footer__rule"></span>
    <span>Weitere Informationen finden Sie auf der Rückseite</span>
    <svg viewBox="0 0 20 20" aria-hidden="true">
      <circle cx="10" cy="10" r="8.5" fill="none" stroke="#fff" stroke-width="1.5"/>
      <path d="M6 10h8M11 7l3 3-3 3" fill="none" stroke="#fff" stroke-width="1.5" stroke-linecap="round" stroke-linejoin="round"/>
    </svg>
  </footer>
</section>

<section class="card card--back" aria-label="Rückseite">
  <div class="back-copy">
    <p>Denn wir gehen mit viel Herz für Sie die sprichwörtliche Extrameile. Genau das ist es, was den Unterschied macht: einen Mehrwert durch beste fachliche Qualifizierung, hohes Engagement, Ehrlichkeit und Fingerspitzengefühl zu schaffen. Eine Entscheidung fürs Leben. Wir begleiten Sie sehr gerne. Wissen, woran man ist. Kennen Sie den wirklich erzielbaren Wert Ihrer Immobilie? Wir schon!</p>
    <p>Lassen Sie sich unverbindlich und kostenfrei beraten. Gerne kommen wir Sie und Ihre Immobilie besuchen und beantworten Ihnen alle<br>Fragen rund um den Verkauf oder die Vermietung Ihrer Immobilie. Nutzen Sie hierfür einfach unseren Gutschein zur kostenlosen Wertermittlung.</p>
    <p>Wir freuen uns auf Ihren Anruf!</p>
  </div>
  <div class="voucher">
    <p class="voucher__title">Gutschein für eine kostenlose Immobilienbewertung</p>
    <p class="voucher__value">im Wert von <strong>500,-€</strong></p>
  </div>
  <div class="gold-rule"></div>
  <aside class="contact-panel">
    <div class="brand">Hülsing Immobilien</div>
    <div class="contact-portrait">
      <div class="photo-portrait" role="img" aria-label="Porträtfoto der Maklerin an einer Tür"></div>
    </div>
    <div class="contact-details">
      <h2>Margarete <span>Hülsing</span></h2>
      <p>Geschäftsführerin</p>
      <p class="qualification">Kauffrau der Grundstücks-<br>und Wohnungswirtschaft</p>
      <p class="line"><b>Büro :</b> 02241 / 48 37 102</p>
      <p class="line"><b>Mail :</b> mail@huelsing-immobilien.de</p>
      <p class="line"><b>Web :</b> www.huelsing-immobilien.de</p>
    </div>
  </aside>
</section>

</body>
</html>
```